Email marketing for Brightfield Optic Services

I need nice design brochure for e mail marketing telling my customers our services and products, location, etc.
At Brightfield Optic Services, we have 25 plus years of combined experience servicing ophthalmic equipment. We offer reliable, timely and economic repairs of a variety of new and discontinued equipment, including, but not limited to Exam Chairs and Stands, Phoropters, Slit Lamps, Keratometers, Hand-helds, BIO’s, Auto Lensmeters, AutoRefractors, Non-Contact Tonometers, Goldman Tonometers, Vira-Tips and many more.

We service all major brands such as: Vell Dorran, Tilsa, Quaven, Fendworth, Ulmbrook, Parsivel, Kessig and more.
We do Preventative Maintenance, Practice Moving, Office Relocation Consulting, Layout Strategy and Equipment Set Up Solutions.

Target Market(s)

Optometrist, Ophthalmologists, Optical Stores

Font styles to use
Sans Serif

Colors
34a6d7

Requirements
Must have
• We comply with all the safety measure according to BHA. Emphasize more on services, service calls.
Link to my website www.brightfieldoptic.example
We buy, sale and service ophthalmic equipment.
Phoroptor cleaning only 275.00. Please use file 4.
File 3 special price for a limited time 925.00.
File 1, Refractor Breath Shield- 19.00.
File 2, Slit Lamp Breath Shield XL 17.00
Nice to have
• I want nice looking professional design that also assures my customers that we are open for business, we comply with all the safety guidelines.

```html
<!DOCTYPE html>
<html lang="en">
<head>
<meta charset="utf-8">
<title>Brightfield Optic Services – Email</title>
<link href="https://fonts.googleapis.com/css2?family=Roboto:wght@400;500;700&display=swap" rel="stylesheet">
<style>
  :root {
    --frame: #3d3d3d;
    --navy: #1f2a7a;
    --blue: #34a6d7;
    --red: #e8484a;
    --text: #555b63;
    --dark-text: #333a40;
    --rule: #e6e9ee;
    --tint: #eaf3fd;
    --white: #ffffff;
    --footer-dark: #4a4a4a;
  }
  * { box-sizing: border-box; margin: 0; padding: 0; }
  html, body { width: 1200px; height: 3782px; overflow: hidden; }
  body {
    background: var(--frame);
    font-family: "Roboto", Arial, sans-serif;
    color: var(--text);
    position: relative;
  }
  .email {
    position: absolute;
    left: 20px; top: 20px;
    width: 1160px; height: 3742px;
    background: var(--white);
    overflow: hidden;
  }
  .notice {
    height: 81px;
    display: flex; align-items: center; justify-content: center;
    color: var(--navy); font-size: 21px;
  }
  .brand-bar {
    height: 151px; background: var(--navy);
    display: flex; align-items: center; justify-content: center;
  }
  .brand-name {
    color: var(--white); font-size: 34px; font-weight: 400;
    letter-spacing: 3px; text-transform: uppercase;
  }
  .hero {
    height: 524px;
    background: linear-gradient(120deg, #2b3f5e 0%, #4f7aa8 35%, #a9c9e8 70%, #dfeaf6 100%);
  }

  .intro { height: 643px; text-align: center; padding-top: 60px; position: relative; }
  .intro h1 { color: var(--navy); font-size: 56px; font-weight: 700; line-height: 64px; }
  .intro h2 { color: var(--blue); font-size: 50px; font-weight: 700; line-height: 60px; margin-top: 6px; }
  .intro p {
    width: 1010px; margin: 45px auto 0;
    font-size: 24px; line-height: 48px;
  }
  .section-title {
    position: absolute; left: 0; right: 0; top: 548px; height: 48px;
    display: flex; align-items: center; gap: 22px;
  }
  .section-title .line { flex: 1; height: 3px; background: var(--blue); position: relative; }
  .section-title .line.left::after,
  .section-title .line.right::before {
    content: ""; position: absolute; top: -5px; width: 13px; height: 13px;
    border-radius: 50%; background: var(--blue);
  }
  .section-title .line.left::after { right: 0; }
  .section-title .line.right::before { left: 0; }
  .section-title span { color: var(--blue); font-size: 40px; font-weight: 500; line-height: 48px; }

  .products { display: grid; grid-template-columns: 1fr 1fr; height: 1341px; }
  .product {
    text-align: center;
    display: flex; flex-direction: column; align-items: center;
    border-right: 2px solid var(--rule);
  }
  .product:nth-child(2n) { border-right: none; }
  .product:nth-child(-n+2) { height: 644px; padding-top: 5px; border-bottom: 2px solid var(--rule); }
  .product:nth-child(n+3) { height: 697px; padding-top: 54px; }
  .product-photo {
    width: 353px; height: 353px; flex: none; border-radius: 50%;
    border: 8px solid #f1f3f5;
    box-shadow: 0 0 0 2px #e4e7eb;
  }
  .photo-parts { background: radial-gradient(circle, #7d7f84 0%, #c9cacd 45%, #f3f3f3 75%); }
  .photo-refractor { background: radial-gradient(circle at 50% 40%, #9b9a98 0%, #6d6457 55%, #4a3f33 100%); }
  .photo-chart { background: radial-gradient(circle, #3c3f46 0%, #a8aab0 45%, #f4f4f4 70%); }
  .photo-slitlamp { background: radial-gradient(circle at 50% 40%, #d8d6d2 0%, #8e8780 55%, #5b534b 100%); }
  .product h3 { color: var(--blue); font-size: 31px; font-weight: 400; line-height: 40px; margin-top: 48px; }
  .product .price { color: var(--red); font-size: 31px; line-height: 40px; margin-top: 8px; }
  .button {
    display: inline-block; margin-top: 20px;
    width: 222px; height: 58px; line-height: 58px;
    background: var(--blue); color: var(--white);
    font-size: 23px; font-weight: 700; text-decoration: none; border-radius: 2px;
  }

  .checks {
    display: flex; flex-wrap: wrap; justify-content: center;
    column-gap: 28px; margin: 0 auto;
  }
  .checks li {
    list-style: none; display: flex; align-items: center; gap: 12px;
    height: 36px; font-size: 26px;
  }
  .checks svg { width: 26px; height: 26px; flex: none; }

  .other { height: 264px; text-align: center; padding-top: 45px; }
  .other h4 { color: var(--blue); font-size: 31px; font-weight: 700; line-height: 40px; }
  .other .checks { width: 1060px; margin-top: 33px; row-gap: 16px; }
  .other .checks li { color: var(--text); }

  .brands { height: 353px; background: var(--tint); text-align: center; padding-top: 84px; }
  .brands h4 { color: var(--blue); font-size: 40px; font-weight: 500; line-height: 48px; }
  .brands .checks { width: 900px; margin-top: 29px; column-gap: 22px; row-gap: 17px; }
  .brands .checks li { font-size: 28px; color: var(--dark-text); }

  .contact {
    height: 302px; background: var(--blue); color: var(--white);
    text-align: center; font-size: 24px; line-height: 40px; padding-top: 33px;
  }
  .contact strong { font-weight: 700; display: block; }
  .contact .hours { margin-top: 23px; }
  .contact a { color: var(--white); text-decoration: none; }
  .legal {
    height: 83px; background: var(--footer-dark); color: var(--white);
    display: flex; align-items: center; justify-content: center; font-size: 24px;
  }
</style>
</head>
<body>
<main class="email">
  <div class="notice">We are open for business, we comply with all the safety guidelines.</div>
  <header class="brand-bar"><span class="brand-name">Brightfield Optic Services</span></header>
  <div class="hero" role="img" aria-label="Close-up photograph of the eyepieces of an ophthalmic slit lamp microscope"></div>

  <section class="intro">
    <h1>WE BUY, SALE AND SERVICE</h1>
    <h2>OPHTHALMIC EQUIPMENT</h2>
    <p>At Brightfield Optic Services, we have 25 plus years of combined experience servicing ophthalmic equipment. We offer reliable, timely and economic repairs of a variety of new and discontinued equipment, including, but not limited to Exam Chairs and Stands, Phoropters, Slit Lamps, Keratometers, Hand-helds, BIO’s, Auto Lensmeters, AutoRefractors, Non-Contact Tonometers, Goldman Tonometers, Vira-Tips and many more.</p>
    <div class="section-title"><i class="line left"></i><span>Brightfield Optic Services</span><i class="line right"></i></div>
  </section>

  <section class="products">
    <article class="product">
      <div class="product-photo photo-parts" role="img" aria-label="Disassembled phoropter parts laid out for cleaning"></div>
      <h3>Phoroptor Cleaning</h3>
      <div class="price">Only 275.00.</div>
      <a class="button" href="https://www.brightfieldoptic.example">View More...</a>
    </article>
    <article class="product">
      <div class="product-photo photo-refractor" role="img" aria-label="Refractor fitted with a clear breath shield"></div>
      <h3>Refractor Breath Shield for</h3>
      <div class="price">Limited time 19.00.</div>
      <a class="button" href="https://www.brightfieldoptic.example">View More...</a>
    </article>
    <article class="product">
      <div class="product-photo photo-chart" role="img" aria-label="24 inch HD acuity chart monitor with remote control"></div>
      <h3>24" HD Acuity Chart for</h3>
      <div class="price">Only 925.00.</div>
      <a class="button" href="https://www.brightfieldoptic.example">View More...</a>
    </article>
    <article class="product">
      <div class="product-photo photo-slitlamp" role="img" aria-label="Slit lamp with an XL breath shield"></div>
      <h3>Slit Lamp Breath Shield XL</h3>
      <div class="price">Only 17.00.</div>
      <a class="button" href="https://www.brightfieldoptic.example">View More...</a>
    </article>
  </section>

  <section class="other">
    <h4>Our Other Services</h4>
    <ul class="checks">
      <li><svg viewBox="0 0 26 26"><rect x="1" y="5" width="19" height="19" fill="none" stroke="#34a6d7" stroke-width="2"/><path d="M5 13l5 5L24 3" fill="none" stroke="#34a6d7" stroke-width="3"/></svg>Preventative Maintenance</li>
      <li><svg viewBox="0 0 26 26"><rect x="1" y="5" width="19" height="19" fill="none" stroke="#34a6d7" stroke-width="2"/><path d="M5 13l5 5L24 3" fill="none" stroke="#34a6d7" stroke-width="3"/></svg>Practice Moving</li>
      <li><svg viewBox="0 0 26 26"><rect x="1" y="5" width="19" height="19" fill="none" stroke="#34a6d7" stroke-width="2"/><path d="M5 13l5 5L24 3" fill="none" stroke="#34a6d7" stroke-width="3"/></svg>Office Relocation Consulting</li>
      <li><svg viewBox="0 0 26 26"><rect x="1" y="5" width="19" height="19" fill="none" stroke="#34a6d7" stroke-width="2"/><path d="M5 13l5 5L24 3" fill="none" stroke="#34a6d7" stroke-width="3"/></svg>Layout Strategy and Equipment</li>
      <li><svg viewBox="0 0 26 26"><rect x="1" y="5" width="19" height="19" fill="none" stroke="#34a6d7" stroke-width="2"/><path d="M5 13l5 5L24 3" fill="none" stroke="#34a6d7" stroke-width="3"/></svg>Set Up Solutions.</li>
    </ul>
  </section>

  <section class="brands">
    <h4>We service all major brands such as</h4>
    <ul class="checks">
      <li><svg viewBox="0 0 26 26"><rect x="1" y="5" width="19" height="19" fill="none" stroke="#34a6d7" stroke-width="2"/><path d="M5 13l5 5L24 3" fill="none" stroke="#34a6d7" stroke-width="3"/></svg>Vell Dorran</li>
      <li><svg viewBox="0 0 26 26"><rect x="1" y="5" width="19" height="19" fill="none" stroke="#34a6d7" stroke-width="2"/><path d="M5 13l5 5L24 3" fill="none" stroke="#34a6d7" stroke-width="3"/></svg>Tilsa</li>
      <li><svg viewBox="0 0 26 26"><rect x="1" y="5" width="19" height="19" fill="none" stroke="#34a6d7" stroke-width="2"/><path d="M5 13l5 5L24 3" fill="none" stroke="#34a6d7" stroke-width="3"/></svg>Quaven</li>
      <li><svg viewBox="0 0 26 26"><rect x="1" y="5" width="19" height="19" fill="none" stroke="#34a6d7" stroke-width="2"/><path d="M5 13l5 5L24 3" fill="none" stroke="#34a6d7" stroke-width="3"/></svg>Fendworth</li>
      <li><svg viewBox="0 0 26 26"><rect x="1" y="5" width="19" height="19" fill="none" stroke="#34a6d7" stroke-width="2"/><path d="M5 13l5 5L24 3" fill="none" stroke="#34a6d7" stroke-width="3"/></svg>Ulmbrook</li>
      <li><svg viewBox="0 0 26 26"><rect x="1" y="5" width="19" height="19" fill="none" stroke="#34a6d7" stroke-width="2"/><path d="M5 13l5 5L24 3" fill="none" stroke="#34a6d7" stroke-width="3"/></svg>Parsivel</li>
      <li><svg viewBox="0 0 26 26"><rect x="1" y="5" width="19" height="19" fill="none" stroke="#34a6d7" stroke-width="2"/><path d="M5 13l5 5L24 3" fill="none" stroke="#34a6d7" stroke-width="3"/></svg>Kessig and more.</li>
    </ul>
  </section>

  <footer class="contact">
    <strong>Store Location :</strong>
    <div>Brightfield Optic Services, Inc.</div>
    <div>418 Linden Ave. Fairhaven, IL 60099 • Tel. 555-014-2237 • E-mail: <a href="mailto:info@brightfieldoptic.example">info@brightfieldoptic.example</a></div>
    <strong class="hours">Business Hours :</strong>
    <div>Monday - Friday: 10AM - 5PM • &nbsp;Saturday: By Appointment • Sunday: By Appointment</div>
  </footer>
  <div class="legal">© Brightfield Optic Services, Inc.</div>
</main>
</body>
</html>
```